Wooden Floor Website

I'd like a Modern and crisp site with emphasis on the site being easy to navigate through - services that we offer, gallery of previous work, history, who we are, contact, etc
https://vaultqx8261937-my.filedeckly.com/:b:/g/personal/tobias_pellwickhaus_co_uk/QWM7R2_kpLsTbNVafrxHoZWCKdYeP8u3G6vRPMsLmoXBtc

Coded - Design and coding required

5+ page

• Word Press Site

```html
<!DOCTYPE html>
<html lang="en">
<head>
<meta charset="utf-8">
<title>Pellwickhaus – Wooden Floors</title>
<link rel="stylesheet" href="https://fonts.googleapis.com/css2?family=IBM+Plex+Sans:wght@400;600;700&family=Open+Sans:wght@400;600;700&family=Playfair+Display:wght@700&display=swap">
<style>
:root{
  --ink:#1f1f1f;
  --text:#555;
  --white:#fff;
  --paper:#f7f7f7;
  --wood:#d97a22;
  --wood-deep:#b9560f;
  --lime:#b8d40f;
  --brown:#3b1d16;
  --curl:#f1e6cc;
  --curl-deep:#dcc597;
}
*{box-sizing:border-box;margin:0;padding:0}
html,body{width:1200px;height:4255px;overflow:hidden}
body{position:relative;font-family:"Open Sans",Arial,sans-serif;color:var(--text);background:var(--white)}
section,header,footer{position:absolute;left:0;width:1200px;overflow:hidden}
.ph{position:absolute;display:block}
h2,h3,h4{font-family:"IBM Plex Sans",Arial,sans-serif;color:var(--ink)}
p{font-size:11px;line-height:1.6}

/* photo tones */
.tone-oak{background:
  radial-gradient(ellipse 60% 40% at 50% 30%,rgba(255,255,255,.55),transparent 70%),
  linear-gradient(180deg,#e3ddd2 0%,#d3c8b6 48%,#b08a60 62%,#8a6642 100%)}
.tone-navy{background:
  radial-gradient(ellipse 40% 30% at 70% 30%,rgba(120,150,180,.5),transparent 70%),
  linear-gradient(180deg,#26364c 0%,#34465e 52%,#a98259 64%,#7c5b3d 100%)}
.tone-green{background:
  radial-gradient(ellipse 35% 25% at 30% 35%,rgba(170,200,160,.45),transparent 70%),
  linear-gradient(180deg,#3f5d4c 0%,#4b6a57 52%,#a27a52 64%,#7a5a3c 100%)}
.tone-warm{background:
  radial-gradient(ellipse 40% 30% at 45% 58%,rgba(225,120,55,.85),transparent 70%),
  linear-gradient(180deg,#ece7df 0%,#ddd5c9 50%,#c09467 63%,#96704a 100%)}
.curl{border-radius:46% 54% 40% 60%;background:
  radial-gradient(ellipse at 35% 30%,rgba(255,255,255,.75),transparent 55%),
  linear-gradient(135deg,var(--curl),var(--curl-deep));opacity:.9}

/* hero */
.hero{top:0;height:681px}
.hero-photo{inset:0;background:
  radial-gradient(ellipse 11% 20% at 80% 36%,rgba(140,190,100,.85),transparent 75%),
  radial-gradient(ellipse 16% 30% at 80% 38%,rgba(255,255,255,.9),transparent 80%),
  radial-gradient(ellipse 22% 8% at 20% 62%,rgba(250,250,250,.95),transparent 75%),
  radial-gradient(ellipse 20% 7% at 86% 62%,rgba(245,245,245,.9),transparent 75%),
  radial-gradient(ellipse 18% 35% at 8% 28%,rgba(150,150,150,.35),transparent 75%),
  linear-gradient(180deg,#8f8f8f 0%,#cfcfcf 6%,#e4e4e4 30%,#d9d9d9 56%,#a9a39c 68%,#5e4838 78%,#3c2b20 100%)}
.main-nav{position:absolute;top:8px;right:38px;display:flex;gap:13px;align-items:center;font:700 10.5px "Open Sans",Arial,sans-serif;color:#222;letter-spacing:.2px}
.main-nav a{color:inherit;text-decoration:none}
.main-nav .current{border-bottom:2px solid #222}
.brand{position:absolute;left:222px;top:282px;font:600 38px "IBM Plex Sans",Arial,sans-serif;letter-spacing:3px;color:#222}
.brand-mark{position:absolute;left:330px;top:112px;width:84px;height:84px;border:3px solid #222}
.trial-panel{position:absolute;left:462px;top:326px;width:318px;height:300px;background:rgba(105,105,105,.6);color:var(--white)}
.trial-panel h3{font:400 18px "Open Sans",Arial,sans-serif;color:var(--white);text-align:center;margin-top:28px}
.field{position:absolute;left:28px;width:262px;border-bottom:1px solid rgba(255,255,255,.6);font-size:11px;padding-bottom:4px}
.field small{display:block;font-size:8.5px;opacity:.8}
.trial-btn{position:absolute;left:58px;top:244px;width:150px;height:24px;background:var(--lime);color:#222;font:700 9.5px "Open Sans",Arial,sans-serif;text-align:center;line-height:24px}
.chevron{position:absolute;left:588px;top:634px}

/* intro */
.intro{top:681px;height:284px;background:var(--white)}
.intro h2{position:absolute;left:247px;top:44px;width:340px;font-size:26px;line-height:1.2}
.intro .p1{position:absolute;left:247px;top:134px;width:310px}
.intro .p2{position:absolute;left:247px;top:178px;width:310px}
.benefit{position:absolute;top:59px;width:165px}
.benefit .ph{position:relative;height:86px}
.benefit h4{font-size:14px;margin:22px 0 6px}
.benefit p{font-size:10.5px}

/* features */
.features{top:965px;height:528px;background:var(--paper)}
.section-title{position:absolute;left:0;width:1200px;text-align:center;font-size:26px;font-weight:600}
.section-sub{position:absolute;left:450px;width:300px;text-align:center;font-size:10.5px}
.feature{position:absolute;left:620px;width:320px;display:flex;gap:20px}
.feature h4{font-size:12.5px;font-weight:600;margin:2px 0 6px}
.feature p{font-size:10.5px}

/* strip */
.strip{top:1493px;height:218px;display:flex;gap:2px;background:#222}
.strip .ph{position:relative;flex:1}

/* faq */
.faq{top:1711px;height:695px;background:
  radial-gradient(ellipse 9% 12% at 57% 57%,rgba(150,70,10,.6),transparent 75%),
  radial-gradient(ellipse 18% 24% at 57% 57%,rgba(240,160,70,.5),transparent 75%),
  repeating-linear-gradient(100deg,rgba(160,70,10,.08) 0 6px,transparent 6px 22px),
  linear-gradient(160deg,#eb9a3a 0%,var(--wood) 45%,var(--wood-deep) 100%)}
.faq .section-title{top:42px}
.faq .section-sub{top:84px;color:#333}
.qa{position:absolute}
.qa h4{font-size:14px;font-weight:600;margin-bottom:12px}
.qa p{font-size:10.5px;color:#2a2a2a}
.faq .feature-block{position:absolute;left:240px;top:448px;width:330px}
.faq .feature-block h2{font-size:26px;line-height:1.2;margin-bottom:18px}
.faq .feature-block p{font-size:10.5px;color:#2a2a2a;margin-bottom:12px}
.avatar{position:absolute;left:688px;top:474px;width:88px;height:88px;border-radius:50%;background:linear-gradient(#dbeaf5,#a9c3d8);border:4px solid var(--white)}
.quote{position:absolute;left:592px;top:566px;width:280px;text-align:center}
.quote p{font-size:11px;font-weight:700;color:#1a1a1a;line-height:1.5}
.quote small{display:block;margin-top:14px;font-size:9.5px;color:#222}
.faq-mark{position:absolute;left:934px;top:322px;width:150px;height:150px;border:4px solid #111}

/* press */
.press{top:2406px;height:199px;background:var(--white)}
.press-name{position:absolute;top:66px;font:700 24px "Playfair Display",Georgia,serif;color:#5a5a5a}
.dots{position:absolute;top:152px;left:551px;display:flex;gap:10px}
.dots i{width:11px;height:11px;border-radius:50%;border:1.5px solid #777}
.dots i.on{background:#777}

/* work */
.work{top:2605px;height:1182px;background:var(--paper)}
.work .section-title{top:162px}
.work-grid{position:absolute;left:176px;top:368px;width:854px;height:468px;display:grid;grid-template-columns:repeat(4,1fr);grid-template-rows:repeat(3,1fr);gap:2px}
.work-grid .ph{position:relative}
.load-more{position:absolute;left:539px;top:893px;width:128px;height:42px;background:var(--brown);border:1px solid #7a2c22;color:var(--white);font:700 11px "Open Sans",Arial,sans-serif;display:flex;align-items:center;justify-content:center;gap:8px;box-shadow:0 2px 4px rgba(0,0,0,.35)}

/* contact */
.contact{top:3787px;height:468px;background:
  repeating-linear-gradient(90deg,rgba(120,40,5,.12) 0 3px,transparent 3px 14px),
  linear-gradient(90deg,#c2591a,#cc6a22 60%,#b9531a)}
.contact-panel{position:absolute;left:43px;top:14px;width:700px;height:355px;background:var(--white)}
.contact-info{position:absolute;left:290px;top:12px;width:390px}
.contact-info h4{font-size:12px;font-weight:600;letter-spacing:1px;margin-bottom:22px}
.contact-info p{font-size:8.5px;line-height:1.5}
.contact-info ul{list-style:none;margin-top:8px;font-size:8.5px}
.contact-info li{display:flex;gap:6px;align-items:center;margin-bottom:3px}
.input{position:absolute;height:18px;border-bottom:1px solid #ccc;font-size:7.5px;color:#777;padding:4px 6px;background:var(--white)}
.send-btn{position:absolute;left:48px;top:378px;padding:4px 10px;background:#1e1e1e;color:var(--white);font:700 7.5px "Open Sans",Arial,sans-serif}
.footer-brand{position:absolute;left:843px;top:128px;font:600 26px "IBM Plex Sans",Arial,sans-serif;letter-spacing:2px;color:#1a1a1a;z-index:2}
.footer-mark{position:absolute;left:900px;top:40px;width:60px;height:60px;border:3px solid #1a1a1a}
</style>
</head>
<body>

<header class="hero">
  <div class="ph hero-photo" role="img" aria-label="Bright living room with white sofas, patterned wall, tall window and dark wooden floor"></div>
  <nav class="main-nav">
    <a class="current" href="#">HOME</a><a href="#">ABOUT</a><a href="#">SKILLS</a><a href="#">SERVICE</a><a href="#">WORK</a><a href="#">TESTIMONIAL</a><a href="#">BLOG</a><a href="#">TEAM</a><a href="#">CONTACT</a>
    <svg width="14" height="14" viewBox="0 0 14 14"><circle cx="5.5" cy="5.5" r="4.3" fill="none" stroke="#222" stroke-width="2"/><line x1="8.6" y1="8.6" x2="13" y2="13" stroke="#222" stroke-width="2.2"/></svg>
  </nav>
  <div class="brand-mark"></div>
  <div class="brand">PELLWICKHAUS</div>
  <form class="trial-panel">
    <h3>Apply Now for Free</h3>
    <div class="field" style="top:70px"><small>Email address</small>hello@pellwickhaus.co.uk</div>
    <div class="field" style="top:126px"><small>Preference</small>Mail frequency</div>
    <div class="field" style="top:180px"><small>Phone</small>123 456 789</div>
    <div class="trial-btn">APPLY FOR FREE TRIAL</div>
  </form>
  <svg class="chevron" width="24" height="14" viewBox="0 0 24 14"><polyline points="2,2 12,11 22,2" fill="none" stroke="#fff" stroke-width="2"/></svg>
</header>

<section class="intro">
  <div class="ph" style="left:0;top:-30px;width:230px;height:130px;background:radial-gradient(ellipse 55% 40% at 45% 45%,#7dbb3c,rgba(90,160,40,.5) 45%,rgba(90,160,40,0) 75%)" role="img" aria-label="Green leaves reaching in from the left"></div>
  <h2>This is your first amazing feature and it's awesome!</h2>
  <p class="p1">Quality timber floors fitted with care, sanded smooth and sealed to last for years.</p>
  <p class="p2">From oak planks to herringbone patterns, our team handles every step, from survey and supply to fitting, finishing and aftercare.</p>
  <div class="benefit" style="left:606px"><div class="ph tone-oak" style="background:radial-gradient(ellipse 30% 35% at 30% 35%,rgba(255,255,255,.7),transparent 70%),linear-gradient(180deg,#d9d6d0 0%,#bdb6ab 50%,#5a4a3c 66%,#3e3128 100%)" role="img" aria-label="Living room with dark wooden floor"></div><h4>First Benefit</h4><p>Free survey and quote, with honest advice on the best floor.</p></div>
  <div class="benefit" style="left:786px"><div class="ph tone-green" role="img" aria-label="Green room with wooden floor"></div><h4>Second Benefit</h4><p>Skilled fitters who leave every room clean and tidy.</p></div>
  <div class="benefit" style="left:966px"><div class="ph" style="background:repeating-linear-gradient(95deg,rgba(90,70,50,.12) 0 2px,transparent 2px 18px),linear-gradient(180deg,#d6d0c5,#a8967e 60%,#84705a)" role="img" aria-label="Close view of wooden floor boards"></div><h4>Third Benefit</h4><p>Long guarantee on both materials and workmanship.</p></div>
</section>

<section class="features">
  <h2 class="section-title" style="top:48px">Features</h2>
  <p class="section-sub" style="top:92px">Everything you need for a new floor, handled by one friendly team.</p>
  <div class="ph curl" style="left:1000px;top:115px;width:140px;height:170px;transform:rotate(-25deg)" role="img" aria-label="Curled wood veneer shaving"></div>
  <div class="ph" style="left:247px;top:184px;width:320px;height:292px;background:
    radial-gradient(ellipse 35% 30% at 18% 22%,rgba(70,90,40,.95),transparent 70%),
    linear-gradient(135deg,transparent 55%,rgba(30,30,30,.0) 55%),
    radial-gradient(ellipse 30% 30% at 85% 10%,rgba(30,30,30,.75),transparent 70%),
    repeating-linear-gradient(120deg,rgba(160,130,95,.15) 0 2px,transparent 2px 26px),
    linear-gradient(135deg,#8a7a55 0%,#c9ad86 40%,#dcc7a6 100%)" role="img" aria-label="Light oak floor with patterned rug and house plant"></div>
  <div class="feature" style="top:190px">
    <svg width="20" height="24" viewBox="0 0 20 24"><rect x="3" y="2" width="14" height="20" rx="2" fill="none" stroke="#999" stroke-width="1.5"/><line x1="7" y1="9" x2="13" y2="9" stroke="#999"/><line x1="7" y1="13" x2="13" y2="13" stroke="#999"/></svg>
    <div><h4>Feature number 1</h4><p>Solid and engineered wood floors chosen to suit your room and budget.</p></div>
  </div>
  <div class="feature" style="top:300px">
    <svg width="20" height="24" viewBox="0 0 20 24"><circle cx="10" cy="12" r="8" fill="none" stroke="#999" stroke-width="1.5"/><polyline points="6,12 9,15 14,9" fill="none" stroke="#999" stroke-width="1.5"/></svg>
    <div><h4>Feature number 1</h4><p>Expert sanding and refinishing to bring tired old boards back to life.</p></div>
  </div>
  <div class="feature" style="top:395px">
    <svg width="20" height="24" viewBox="0 0 20 24"><rect x="3" y="5" width="14" height="15" rx="2" fill="none" stroke="#999" stroke-width="1.5"/><line x1="3" y1="10" x2="17" y2="10" stroke="#999"/></svg>
    <div><h4>Feature number 1</h4><p>Clear fixed prices agreed before work starts, with no hidden costs.</p></div>
  </div>
</section>

<section class="strip">
  <div class="ph" style="background:radial-gradient(ellipse 40% 30% at 40% 25%,rgba(255,255,255,.8),transparent 70%),linear-gradient(180deg,#e0ddd6 0%,#c9c4bb 50%,#5d5248 64%,#3c342d 100%)" role="img" aria-label="Hallway with grey wooden floor"></div>
  <div class="ph" style="background:repeating-linear-gradient(45deg,rgba(255,255,255,.08) 0 14px,transparent 14px 28px),repeating-linear-gradient(-45deg,rgba(0,0,0,.1) 0 14px,transparent 14px 28px),linear-gradient(135deg,#8e877c,#5e574e)" role="img" aria-label="Grey herringbone floor"></div>
  <div class="ph" style="background:radial-gradient(ellipse 30% 25% at 60% 25%,rgba(255,255,255,.7),transparent 70%),linear-gradient(180deg,#d0cdc5 0%,#b8b3a9 45%,#5c4e40 60%,#3e342b 100%)" role="img" aria-label="Room with shelves and dark floor"></div>
  <div class="ph" style="background:repeating-linear-gradient(100deg,rgba(255,255,255,.06) 0 2px,transparent 2px 30px),linear-gradient(135deg,#54463a,#2e2620)" role="img" aria-label="Dark oak plank floor"></div>
  <div class="ph" style="background:radial-gradient(ellipse 25% 20% at 45% 40%,rgba(60,70,60,.8),transparent 70%),linear-gradient(180deg,#5a4a3a 0%,#9c7450 35%,#c99866 100%)" role="img" aria-label="Warm wooden floor with record player"></div>
  <div class="ph" style="background:repeating-linear-gradient(45deg,rgba(255,255,255,.08) 0 14px,transparent 14px 28px),repeating-linear-gradient(-45deg,rgba(0,0,0,.1) 0 14px,transparent 14px 28px),linear-gradient(135deg,#8f7b66,#5a4a3c)" role="img" aria-label="Brown herringbone floor"></div>
</section>

<section class="faq">
  <div class="ph" style="left:0;top:0;width:480px;height:460px;background:radial-gradient(ellipse 60% 55% at 25% 40%,rgba(255,255,255,.6),rgba(255,255,255,.2) 50%,rgba(255,255,255,0) 75%)" role="img" aria-label="Faded white checker pattern over wood grain"></div>
  <h2 class="section-title">Frequently Asked Questions</h2>
  <p class="section-sub">Our answers | we're here to help</p>
  <div class="qa" style="left:247px;top:168px;width:310px"><h4>How does the free trial work?</h4><p>Book a visit and we bring samples to your home, measure each room and give a written quote with no obligation.</p></div>
  <div class="qa" style="left:247px;top:282px;width:310px"><h4>Can I switch plans later?</h4><p>Yes, you can change your choice at any time before fitting.</p></div>
  <div class="qa" style="left:605px;top:168px;width:380px"><h4>Do I need to choose plan now?</h4><p>No rush. Take the samples, think it over and call us back whenever you feel ready.</p></div>
  <div class="qa" style="left:605px;top:262px;width:380px"><h4>What payment types do you accept?</h4><p>We take bank transfer, debit card and credit card, with a small deposit to book.</p></div>
  <div class="faq-mark"></div>
  <div class="feature-block">
    <h2>This is your first amazing feature and it's awesome!</h2>
    <p>Every floor we lay is checked twice, so it looks right and feels solid underfoot.</p>
    <p>We work around your schedule and keep dust and noise to a minimum while in.</p>
    <p>Ask about our care kits to keep your new floor looking fresh for years.</p>
  </div>
  <div class="avatar" role="img" aria-label="Portrait of a fitter in a hard hat"></div>
  <div class="quote"><p>„ Great work, on time and tidy. Our new floor looks perfect! "</p><small>Alex Tobias, PELLWICKHAUS</small></div>
</section>

<section class="press">
  <div class="press-name" style="left:285px">Ledgerly</div>
  <div class="press-name" style="left:455px">Harbor Daily</div>
  <div class="press-name" style="left:628px;font-size:16px;top:74px">Market Ledger</div>
  <div class="press-name" style="left:805px;font-family:'IBM Plex Sans',Arial,sans-serif">The Kernel</div>
  <div class="dots"><i></i><i class="on"></i><i></i><i></i></div>
</section>

<section class="work">
  <div class="ph curl" style="left:560px;top:-10px;width:150px;height:250px;transform:rotate(20deg)" role="img" aria-label="Curled wood veneer shaving"></div>
  <div class="ph curl" style="left:440px;top:210px;width:120px;height:170px;transform:rotate(-15deg)" role="img" aria-label="Curled wood veneer shaving"></div>
  <div class="ph curl" style="left:860px;top:30px;width:200px;height:210px" role="img" aria-label="Curled wood veneer shaving"></div>
  <div class="ph curl" style="left:40px;top:210px;width:140px;height:230px;transform:rotate(30deg)" role="img" aria-label="Curled wood veneer shaving"></div>
  <div class="ph curl" style="left:290px;top:880px;width:60px;height:150px;transform:rotate(-20deg)" role="img" aria-label="Curled wood veneer shaving"></div>
  <div class="ph curl" style="left:880px;top:830px;width:200px;height:170px" role="img" aria-label="Curled wood veneer shaving"></div>
  <h2 class="section-title">Our Amazing Work</h2>
  <div class="work-grid">
    <div class="ph tone-oak" role="img" aria-label="Bedroom with oak floor"></div>
    <div class="ph" style="background:radial-gradient(ellipse 50% 35% at 40% 35%,rgba(220,110,40,.9),transparent 70%),linear-gradient(180deg,#b0825a,#8a6440)" role="img" aria-label="Orange sofa on wooden floor"></div>
    <div class="ph" style="background:radial-gradient(ellipse 25% 20% at 40% 55%,rgba(190,110,70,.7),transparent 70%),linear-gradient(180deg,#ece9e3 0%,#dcd6cc 50%,#c4a47f 64%,#a78462 100%)" role="img" aria-label="Dining table on light floor"></div>
    <div class="ph tone-navy" role="img" aria-label="Blue wall room with rug"></div>
    <div class="ph tone-warm" role="img" aria-label="Orange sofa in white room"></div>
    <div class="ph tone-navy" role="img" aria-label="Navy kitchen with oak floor"></div>
    <div class="ph" style="background:radial-gradient(ellipse 30% 20% at 50% 60%,rgba(220,170,110,.6),transparent 70%),linear-gradient(180deg,#24324a 0%,#2c3a52 55%,#8c6a48 66%,#6a4e36 100%)" role="img" aria-label="Dark blue living room"></div>
    <div class="ph" style="background:radial-gradient(ellipse 40% 30% at 55% 40%,rgba(120,60,40,.6),transparent 70%),linear-gradient(180deg,#8a6a52,#a07850)" role="img" aria-label="Wooden chairs on floor"></div>
    <div class="ph tone-green" role="img" aria-label="Green room with herringbone floor"></div>
    <div class="ph" style="background:radial-gradient(ellipse 40% 25% at 50% 55%,rgba(230,225,215,.8),transparent 70%),linear-gradient(180deg,#cfc6b8,#9c7a58)" role="img" aria-label="Rug on oak floor"></div>
    <div class="ph" style="background:repeating-linear-gradient(100deg,rgba(255,255,255,.08) 0 2px,transparent 2px 24px),linear-gradient(180deg,#c19466,#8a643f)" role="img" aria-label="Close view of planks"></div>
    <div class="ph" style="background:radial-gradient(ellipse 30% 20% at 50% 60%,rgba(160,90,60,.6),transparent 70%),linear-gradient(180deg,#2c3448 0%,#323c52 55%,#8a6a4a 66%,#6c5038 100%)" role="img" aria-label="Dining room with dark wall"></div>
  </div>
  <div class="load-more"><svg width="10" height="10" viewBox="0 0 10 10"><path d="M5 0v10M0 5h10" stroke="#fff" stroke-width="2"/></svg>LOAD MORE</div>
</section>

<footer class="contact">
  <div class="contact-panel">
    <div class="ph" style="left:0;top:0;width:262px;height:140px;background:
      linear-gradient(90deg,transparent 48%,rgba(250,200,80,.7) 48% 50%,transparent 50%),
      linear-gradient(0deg,transparent 55%,rgba(250,200,80,.7) 55% 57%,transparent 57%),
      linear-gradient(135deg,#ecebe5,#dfe3e6)" role="img" aria-label="Street map of the showroom area"></div>
    <div class="contact-info">
      <h4>CONTACT INFORMATION</h4>
      <p>Visit our showroom or drop us a line. We reply to every message within one working day and are glad to help.</p>
      <ul>
        <li><svg width="8" height="10" viewBox="0 0 8 10"><path d="M4 0a3.5 3.5 0 0 0-3.5 3.5C.5 6 4 10 4 10s3.5-4 3.5-6.5A3.5 3.5 0 0 0 4 0z" fill="#777"/></svg>Address: 123 Street Name, City Name, United Kingdom</li>
        <li><svg width="9" height="7" viewBox="0 0 9 7"><rect x=".5" y=".5" width="8" height="6" fill="none" stroke="#777"/><path d="M.5.5l4 3 4-3" fill="none" stroke="#777"/></svg>Email: hello@pellwickhaus.co.uk</li>
        <li><svg width="9" height="9" viewBox="0 0 9 9"><circle cx="4.5" cy="4.5" r="4" fill="none" stroke="#777"/></svg>www.pellwickhaus.co.uk</li>
      </ul>
    </div>
  </div>
  <div class="input" style="left:48px;top:180px;width:332px">YOUR NAME</div>
  <div class="input" style="left:400px;top:180px;width:330px">YOUR EMAIL ADDRESS</div>
  <div class="input" style="left:48px;top:208px;width:682px">WEBSITE ADDRESS</div>
  <div class="input" style="left:48px;top:236px;width:682px;height:110px;border-bottom:none">PLEASE WRITE A MESSAGE HERE</div>
  <div class="send-btn">SEND MESSAGE</div>
  <div class="footer-mark"></div>
  <div class="footer-brand">PELLWICKHAUS</div>
  <div class="ph" style="left:800px;top:160px;width:400px;height:240px;background:
    radial-gradient(ellipse 14% 45% at 20% 60%,#3f7a30,transparent 75%),
    radial-gradient(ellipse 12% 50% at 45% 55%,#2f6426,transparent 75%),
    radial-gradient(ellipse 13% 45% at 70% 60%,#3a7230,transparent 75%),
    radial-gradient(ellipse 12% 50% at 92% 55%,#2d5f24,transparent 75%)" role="img" aria-label="Row of green trees"></div>
  <div class="ph" style="left:0;top:380px;width:1200px;height:88px;background:
    radial-gradient(ellipse 12% 60% at 10% 30%,#5e9a36,transparent 75%),
    radial-gradient(ellipse 12% 60% at 40% 30%,#5a9434,transparent 75%),
    radial-gradient(ellipse 12% 60% at 70% 30%,#619d38,transparent 75%),
    linear-gradient(#4d8a2e 30%,#2e5a1c)" role="img" aria-label="Green treetops along the bottom"></div>
</footer>

</body>
</html>
```